NEW Modern Sleek Business Card for VR Language Startup

Our startup is using VR to lead the next wave of world language education. We need a two-sided business card that introduces the larger organization (Quorvel Language Inc) and our contact info on one side and shows the product, Lumidrasca, on the other side.

Side 1 (contact info)= Quorvel Logo and Contact info (name, title, phone, email)

Side 2 (product)= Lumidrasc logo, text, and website
Text= Culturally Immersive Language Learning Games
Website= www.lumidrasc.example

Target Market(s)

Education, Technology

Contact Information for Business Card

Contact info will be updated upon approval of the design. For now, put this as a placeholder.

Perry Hollins
Founder & CEO
phollins@mailtrove.example
(555)-014-2736

Font styles to use
Other font styles liked:
• Gibson and Century Gothic are the brand fonts

Requirements
Nice to have
• I would love to see cohesion between the design and colors of the two logos. I have attached a few business card designs that I like, so you can get a feel for my preferred style.

```html
<!DOCTYPE html>
<html lang="en">
<head>
<meta charset="utf-8">
<title>Quorvel Language – Business Card</title>
<link rel="stylesheet" href="https://fonts.googleapis.com/css2?family=Didact+Gothic&display=swap">
<style>
  :root {
    --card-blue: #175a91;
    --card-white: #ffffff;
    --guide-red: #e3263a;
    --icon-blue: #2aa4e0;
    --ink: #111111;
    --divider: #cfd6dc;
    --mark-blue: #3aa7ea;
    --font-main: "Didact Gothic", "Century Gothic", sans-serif;
  }
  * { box-sizing: border-box; margin: 0; padding: 0; }
  html, body {
    width: 1200px;
    height: 376px;
    overflow: hidden;
    background: var(--card-white);
    font-family: var(--font-main);
  }
  .canvas { position: relative; width: 1200px; height: 376px; }

  .card { position: absolute; overflow: hidden; }
  .card-front { left: 0; top: 5px; width: 587px; height: 361px; }
  .card-back { left: 609px; top: 8px; width: 591px; height: 360px; background: var(--card-blue); }
  .card-art { position: absolute; inset: 0; width: 100%; height: 100%; }

  .sheet-divider {
    position: absolute; left: 602px; top: 0;
    width: 3px; height: 376px; background: var(--divider);
  }

  /* front: company name */
  .company-mark {
    position: absolute; left: 18px; top: 146px;
    width: 48px; height: 48px; border-radius: 50%;
    background: var(--mark-blue);
  }
  .company-name {
    position: absolute; left: 76px; top: 152px;
    color: var(--card-white);
    font-size: 36px; line-height: 1;
    letter-spacing: 0.02em;
    white-space: nowrap;
  }
  .company-sub {
    position: absolute; left: 18px; top: 222px;
    color: var(--card-white);
    font-size: 22px; line-height: 1;
    letter-spacing: 0.95em;
    white-space: nowrap;
  }
  .company-web {
    position: absolute; left: 40px; top: 310px;
    color: var(--card-white);
    font-size: 15px; line-height: 1;
    letter-spacing: 0.58em;
    white-space: nowrap;
  }

  /* front: contact block */
  .contact { position: absolute; right: 35px; text-align: right; color: var(--ink); white-space: nowrap; }
  .contact-name { top: 128px; font-size: 38px; line-height: 1; }
  .contact-title { top: 172px; font-size: 17px; line-height: 1; }
  .contact-line {
    position: absolute; right: 34px;
    display: flex; align-items: center; gap: 8px;
    color: var(--ink); font-size: 14.5px; line-height: 1;
    white-space: nowrap;
  }
  .contact-email { top: 215px; }
  .contact-phone { top: 251px; }
  .contact-icon { width: 23px; height: 23px; flex: none; }

  /* back: product */
  .product-mark {
    position: absolute; left: 241px; top: 38px;
    width: 130px; height: 130px; border-radius: 50%;
    background: var(--mark-blue);
  }
  .product-name {
    position: absolute; left: 0; right: 0; top: 176px;
    text-align: center; color: var(--card-white);
    font-size: 44px; line-height: 1;
  }
  .product-tagline {
    position: absolute; left: 0; right: 0; top: 228px;
    text-align: center; color: var(--card-white);
    font-size: 17px; line-height: 1; letter-spacing: 0.09em;
  }
  .product-web {
    position: absolute; left: 0; right: 0; top: 306px;
    text-align: center; color: var(--card-white);
    font-size: 15px; line-height: 1; letter-spacing: 0.55em;
  }
</style>
</head>
<body>
<main class="canvas">

  <section class="card card-front" aria-label="Business card front">
    <svg class="card-art" viewBox="0 10 1260 775" preserveAspectRatio="none" aria-hidden="true">
      <rect x="0" y="10" width="1260" height="775" fill="var(--card-blue)"/>
      <polygon points="935,10 1260,10 1260,785 935,785 565,385" fill="var(--card-white)"/>
      <polygon points="975,10 1005,10 625,385 1005,785 975,785 595,385" fill="var(--card-blue)"/>
      <rect x="12" y="57" width="1198" height="683" rx="26" fill="none" stroke="var(--guide-red)" stroke-width="4"/>
    </svg>

    <div class="company-mark" aria-hidden="true"></div>
    <div class="company-name">QUORVEL</div>
    <div class="company-sub">LANGUAGE</div>
    <div class="company-web">WWW.QUORVEL.EXAMPLE</div>

    <div class="contact contact-name">Perry Hollins</div>
    <div class="contact contact-title">Founder &amp; CEO</div>

    <div class="contact-line contact-email">
      <span>phollins@mailtrove.example</span>
      <svg class="contact-icon" viewBox="0 0 24 24" aria-hidden="true">
        <rect x="1" y="1" width="22" height="22" fill="var(--icon-blue)" stroke="#9fd3f0" stroke-width="1.5"/>
        <path d="M8 7 L17 11 L13 12.5 L11.5 16.5 Z" fill="var(--card-white)"/>
      </svg>
    </div>
    <div class="contact-line contact-phone">
      <span>(555)-014-2736</span>
      <svg class="contact-icon" viewBox="0 0 24 24" aria-hidden="true">
        <rect x="1" y="1" width="22" height="22" fill="var(--icon-blue)" stroke="#9fd3f0" stroke-width="1.5"/>
        <path d="M6 10 Q12 6 18 10 L17 11.5 L15 10.5 L14.5 9.5 Q12 9 9.5 9.5 L9 10.5 L7 11.5 Z" fill="var(--card-white)"/>
        <rect x="8" y="12" width="8" height="5" rx="1" fill="var(--card-white)"/>
      </svg>
    </div>
  </section>

  <div class="sheet-divider" aria-hidden="true"></div>

  <section class="card card-back" aria-label="Business card back">
    <svg class="card-art" viewBox="0 0 591 360" preserveAspectRatio="none" aria-hidden="true">
      <rect x="16" y="21" width="559" height="318" rx="12" fill="none" stroke="var(--guide-red)" stroke-width="2"/>
    </svg>
    <div class="product-mark" aria-hidden="true"></div>
    <div class="product-name">Lumidrasc</div>
    <div class="product-tagline">Culturally Immersive Language Learning Games</div>
    <div class="product-web">www.lumidrasc.example</div>
  </section>

</main>
</body>
</html>
```